Letterhead Design Project

Consulting Company , we want a letterhead incorporating both the picture provided and the logo provided. The font name is monotype corsiva.
Target Market(s)
Dentist
Industry/Entity Type
Consulting
Font styles to use
Other font styles liked:
- monotype corsiva

Colors
0455a3
Requirements
Must have
- the logo, the picture (see attached), the website name, the email. and the phone numbers.
- Website: www.trquillarisadvisory.solutions
- Email: will be provided to the winner, please use placeholder
- Phone numbers:
- Petra Hallum 5829017763
- Owen Vrastik 6148250397

Nice to have
- a swoop or wave across the bottom. a line up the side. I don't know guys. design something unique and professional.

Should not have
- arrows pointing off the logo or anywhere. no arrows. our logo altered in anyway. no broken circles. no variences in blue. we like our logo the way it is. the font is monotype corsiva

```html
<!DOCTYPE html>
<html lang="en">
<head>
<meta charset="utf-8">
<title>Trquillaris Advisory Letterhead</title>
<link rel="stylesheet" href="https://fonts.googleapis.com/css2?family=Arimo:wght@400;700&family=Cormorant+Garamond:ital,wght@1,600&family=Kaushan+Script&display=swap">
<style>
  :root {
    --brand-blue: #0455a3;
    --band-grey: #4a5058;
    --paper: #f3f3f4;
    --backdrop: #e6e7e9;
    --ink: #1d1d1f;
    --muted-ink: #3a3a3d;
    --white: #ffffff;
  }
  * { box-sizing: border-box; margin: 0; padding: 0; }
  html, body { width: 1200px; height: 795px; overflow: hidden; }
  body {
    background: var(--backdrop);
    display: flex; align-items: center; justify-content: center;
    font-family: "Arimo", Arial, sans-serif;
    color: var(--ink);
  }
  .letterhead {
    position: relative;
    width: 540px; height: 764px;
    background: var(--paper);
    box-shadow: 0 4px 18px rgba(0,0,0,0.12);
    overflow: hidden;
  }
  .header-art { position: absolute; left: 0; top: 0; z-index: 1; }
  .brand {
    position: absolute; left: 94px; top: 50px; z-index: 2;
    font-family: "Cormorant Garamond", serif;
    color: var(--brand-blue);
    white-space: nowrap;
  }
  .brand-name { font-size: 17px; font-weight: 600; font-style: italic; line-height: 1; }
  .brand-address { font-size: 9px; color: var(--muted-ink); line-height: 1.2; margin-top: 3px; font-style: italic; font-weight: 600; }
  .recipient {
    position: absolute; left: 60px; top: 142px;
    font-size: 10px; line-height: 1.15;
  }
  .recipient-name { font-weight: 700; font-size: 11px; }
  .letter-body {
    position: absolute; left: 60px; top: 196px; width: 410px;
    font-size: 9.6px; line-height: 1.42; color: var(--ink);
  }
  .letter-body p { margin-bottom: 14px; }
  .closing { font-size: 9.6px; }
  .sign-off { margin-top: 10px; padding-left: 10px; }
  .signature {
    font-family: "Kaushan Script", cursive;
    font-size: 38px; color: var(--ink); line-height: 1.1;
  }
  .signatory {
    margin-top: 6px; padding-left: 16px;
    font-size: 10.5px; font-weight: 700; line-height: 1.2;
  }
  .footer-art { position: absolute; left: 0; bottom: 0; }
  .contact-phones {
    position: absolute; left: 40px; bottom: 44px;
    color: var(--white); font-size: 11px; font-weight: 700; letter-spacing: 0.2px;
    white-space: nowrap;
  }
  .contact-phones .number { font-weight: 400; }
  .contact-phones .divider { margin: 0 12px; font-weight: 400; }
  .contact-web {
    position: absolute; left: 52px; bottom: 13px;
    color: var(--white); font-family: "Cormorant Garamond", serif;
    font-style: italic; font-weight: 600; font-size: 12px;
    white-space: nowrap;
  }
  .contact-web .divider { margin: 0 6px; }
  .portrait {
    position: absolute; right: 26px; bottom: 76px;
    width: 112px; height: 112px; border-radius: 50%;
    border: 4px solid var(--brand-blue);
    background: var(--paper);
    padding: 5px;
  }
  .portrait-fill {
    width: 100%; height: 100%; border-radius: 50%;
    background: radial-gradient(circle at 45% 38%, #a9a9ab 0%, #6c6c6f 45%, #2a2a2c 100%);
  }
</style>
</head>
<body>
  <main class="letterhead">
    <svg class="header-art" width="320" height="110" viewBox="0 0 320 110" aria-hidden="true">
      <polygon points="0,52 78,52 70,70 0,70" fill="var(--brand-blue)"/>
      <line x1="96" y1="44" x2="300" y2="44" stroke="var(--brand-blue)" stroke-width="3"/>
      <line x1="112" y1="38" x2="286" y2="38" stroke="var(--brand-blue)" stroke-width="3"/>
      <line x1="128" y1="32" x2="272" y2="32" stroke="var(--brand-blue)" stroke-width="3"/>
      <circle cx="52" cy="61" r="26" fill="var(--paper)" stroke="var(--brand-blue)" stroke-width="4"/>
    </svg>
    <div class="brand">
      <div class="brand-name">Trquillaris Advisory, LLC</div>
      <div class="brand-address">418 Alder Lane<br>Brookhaven, Ohio 43017</div>
    </div>

    <div class="recipient">
      <div class="recipient-name">JOHN SMITH</div>
      <div>Street Name,City Name.</div>
      <div>Zip Coad 0000</div>
    </div>

    <section class="letter-body">
      <p>Lorem Ipsum is simply dummy text of the printing and typesetting industry. Lorem Ipsum has been the industry's standard dummy text ever since the 1500s, when an unknown printer took a galley of type and scrambled it to make a type specimen book. It has survived not only five centuries,but also the leap into electronic typesetting, remaining essentially unchanged. It was popularised in the 1960s with the release of Letraset sheets containing Lorem Ipsum passages, and more recently with desktop publishing software like Aldus PageMaker including versions of Lorem Ipsum.</p>
      <p>It is a long established fact that a reader will be distracted by the readable content of a page when looking at its layout. The point of using Lorem Ipsum is that it has a more-or-less normal distribution of letters, as opposed to using 'Content here, content here', making it look like readable English. Many desktop and publishing packages and web page editors now use Lorem Ipsum as their default model text, and a search for 'lorem ipsum' will uncover many web sites still in their infancy. Various versions have evolved over the years, sometimes by accident, sometimes on purpose (injected humour and the like).</p>
      <div class="closing">Regards,</div>
      <div class="sign-off">
        <div class="signature">John Doe</div>
        <div class="signatory">John Doe<br>General Manager</div>
      </div>
    </section>

    <div class="portrait"><div class="portrait-fill" role="img" aria-label="Portrait photograph of the company representative"></div></div>

    <svg class="footer-art" width="540" height="80" viewBox="0 0 540 80" aria-hidden="true">
      <polygon points="16,22 540,22 540,50 6,50" fill="var(--band-grey)"/>
      <polygon points="6,50 540,50 540,80 0,80" fill="var(--brand-blue)"/>
      <polygon points="0,22 16,22 6,50 0,50" fill="var(--paper)"/>
    </svg>
    <div class="contact-phones">PETRA HALLUM <span class="number">5829017763</span><span class="divider">|</span>OWEN VRASTIK <span class="number">6148250397</span></div>
    <div class="contact-web">info@yourcompanymail.com<span class="divider">|</span>www.trquillarisadvisory.solutions</div>
  </main>
</body>
</html>
```